Postcard and Door Hanger Design

We need two pieces designed for marketing. Both will use the same logo and photo just the text will be slightly different. We need these designs looking very modern, clean, and simple while having the important information to stand out.

Postcard: 2 sided
- Side 1 just have large logo with our website and phone number
- Side 2 below.
- 4 x 6
- Use photo of house provided
- "Going Above and Beyond Every Time"
- "Call TODAY to Reserve your project by May 1st and receive 10% off"
- "Residential and Commercial"
- Our contact is 250-555-0147
- Website is www.brightoakcoatings.com
- Might include something like "check out our portfolio on our website"

Use the above as a guidline and be creative with it, add or take away as you see fit as we are open to suggestions.

Door Hanger: 2 sided
Side 1 - Logo with contact details
Side 2 - Below
- 4 x 11
- "We are painting your neighborhood"
-"come see us in action at (then leave a space where we can stick a label onto our door hanger with an address of a home we are painting)
- Call today for a FREE ESTIMATE
- 250-555-0147
- www.brightoakcoatings.com

https://www.filenook.net/sh/42qrt19k3mzp5xa/RT7KLMN-QZ

https://www.filenook.net/sh/tt3ru58w7jxe21c/LMwRRJnoQx

https://www.filenook.net/sh/p3z55rf6wqn44dd/xvt-Hj2KWa

```html
<!DOCTYPE html>
<html lang="en">
<head>
<meta charset="utf-8">
<title>Bright Oak Coatings – Postcard</title>
<link rel="stylesheet" href="https://fonts.googleapis.com/css2?family=Cinzel:wght@400&family=Crimson+Pro:ital,wght@0,400;0,700;1,600&display=swap">
<style>
  :root{
    --teal:#1aaaa5;
    --teal-deep:#15928e;
    --slate:#4a4f58;
    --ink:#353a40;
    --mist:#d6eef0;
    --white:#ffffff;
  }
  html,body{margin:0;padding:0;overflow:hidden;background:#fff;}
  .postcard{position:relative;width:800px;height:1200px;overflow:hidden;background:var(--teal);}
  .hero-photo{position:absolute;left:0;top:0;width:800px;height:636px;
    background:linear-gradient(180deg,#2e6fc4 0%,#6aa2db 28%,#5b6a5a 45%,#4f5556 58%,#3f6b36 75%,#5c8a3c 100%);}
  .offer-band{position:absolute;left:0;top:636px;width:800px;height:419px;background:var(--teal);}
  .headline{position:absolute;left:107px;top:650px;margin:0;
    font-family:"Cinzel",serif;font-weight:400;font-size:60px;line-height:59px;color:var(--ink);letter-spacing:0.5px;}
  .headline span{display:block;}
  .feature{position:absolute;left:425px;top:636px;width:340px;height:255px;background:var(--slate);}
  .feature-photo{position:absolute;left:8px;top:0;width:324px;height:212px;
    background:linear-gradient(160deg,#e8e2da 0%,#8a7566 45%,#4a3c33 75%,#2f2a27 100%);}
  .feature-caption{position:absolute;left:0;top:212px;width:340px;height:43px;
    font-family:"Crimson Pro",serif;font-style:italic;font-weight:600;font-size:25px;line-height:43px;
    color:var(--white);text-align:center;letter-spacing:1px;}
  .callout{position:absolute;left:432px;top:908px;width:368px;height:114px;background:var(--mist);}
  .callout-brace{position:absolute;left:408px;top:905px;}
  .callout p{margin:0;padding:12px 0 0 18px;font-family:"Crimson Pro",serif;font-size:24px;line-height:29px;color:var(--ink);}
  .callout strong{font-weight:700;}
  .footer{position:absolute;left:0;top:1055px;width:800px;height:115px;background:var(--slate);}
  .footer-strip{position:absolute;left:0;top:1170px;width:800px;height:30px;background:var(--teal);}
  .brand{position:absolute;left:28px;top:1075px;display:flex;align-items:center;gap:20px;}
  .brand-mark{width:52px;height:75px;background:var(--teal);}
  .brand-name{font-family:"Cinzel",serif;font-weight:400;color:var(--white);line-height:1;}
  .brand-name .top{display:block;font-size:38px;letter-spacing:2px;}
  .brand-name .bottom{display:block;font-size:20px;letter-spacing:8px;margin-top:8px;}
  .contact{position:absolute;left:428px;top:1078px;font-family:"Crimson Pro",serif;color:var(--white);}
  .contact-row{display:flex;align-items:center;gap:10px;height:36px;}
  .contact .phone{font-size:30px;}
  .contact .web{font-size:25px;}
</style>
</head>
<body>
<div class="postcard">
  <div class="hero-photo" role="img" aria-label="Photo of a freshly painted grey two-storey house with white trim, white garage door and landscaped shrubs under a blue sky"></div>

  <section class="offer-band">
  </section>
  <h1 class="headline"><span>Going</span><span>Above</span><span>And</span><span>Beyond</span><span>Every</span><span>Time</span></h1>

  <figure class="feature" style="margin:0">
    <div class="feature-photo" role="img" aria-label="Photo of a modern painted kitchen interior with island and bar stools"></div>
    <figcaption class="feature-caption">Residential &amp; Commercial</figcaption>
  </figure>

  <svg class="callout-brace" width="26" height="120" viewBox="0 0 26 120" aria-hidden="true">
    <path d="M22 3 Q12 3 12 14 L12 48 Q12 58 3 60 Q12 62 12 72 L12 106 Q12 117 22 117" fill="none" stroke="var(--slate)" stroke-width="4"/>
  </svg>
  <div class="callout">
    <p><strong>Call TODAY</strong> to Reserve<br>your project by May 1st<br>and receive <strong>10% off</strong></p>
  </div>

  <footer class="footer"></footer>
  <div class="brand">
    <div class="brand-mark"></div>
    <div class="brand-name"><span class="top">BRIGHT OAK</span><span class="bottom">COATINGS</span></div>
  </div>
  <div class="contact">
    <div class="contact-row">
      <svg width="22" height="22" viewBox="0 0 24 24" aria-hidden="true"><path d="M6.6 10.8c1.4 2.8 3.8 5.1 6.6 6.6l2.2-2.2c.3-.3.7-.4 1-.2 1.1.4 2.3.6 3.6.6.6 0 1 .4 1 1V20c0 .6-.4 1-1 1C10.6 21 3 13.4 3 4c0-.6.4-1 1-1h3.5c.6 0 1 .4 1 1 0 1.3.2 2.5.6 3.6.1.3 0 .7-.2 1L6.6 10.8z" fill="var(--teal)"/></svg>
      <span class="phone">250-555-0147</span>
    </div>
    <div class="contact-row">
      <svg width="22" height="22" viewBox="0 0 24 24" aria-hidden="true"><circle cx="12" cy="12" r="10" fill="var(--teal)"/><path d="M2 12h20M12 2c3 3 3 17 0 20M12 2c-3 3-3 17 0 20M4.5 6.5h15M4.5 17.5h15" stroke="var(--slate)" stroke-width="1.3" fill="none"/></svg>
      <span class="web">www.brightoakcoatings.com</span>
    </div>
  </div>
  <div class="footer-strip"></div>
</div>
</body>
</html>
```